I’d like to see something with similar colors and design concept to the “Your Fortune Starts at Breakfast” book included in attchment

Create a book cover with front cover, and full front, spine and back cover spread.
Simple and clean design. See design inspiration below.
Size 6X9
Title of the book: Write Onward! Veteran Editors Reveal Their Methods

Please leave space for 6 authors names on the front cover. Authors names will be provided at a later time.

Back of book should included the name of the publishing company:
Bright Lantern Publishing

As well as the following synopsis
The landscape of the publishing industry is changing. Gone are the days of coveted gatekeepers controlling content and dictating the messages being distributed. With the rise of technology, social media , self-publishing platforms, and independent bookstores, there are increased opportunities for people to share their ideas, messages, and stories with the world through books. The types of books that we’re publishing are also evolving — mini-books, audio books, journals, multi-author books, cook books, children’s books, comic books, coloring books, interactive books, tarot and oracle card decks are all expanding the podium for people to express ideas and influence the culture. More and more entrepreneurs are posturing themselves as thought leaders by leveraging this growing platform.
But that doesn't mean it’s easy.
Even with the expanding platforms and opportunities, only a fraction of people with publishing ambitions are able to achieve this coveted dream held by so many. It can be a daunting process for budding authors trying to maneuver through the writing, packaging, marketing, and publishing processes alone.

In this book you'll find passionate, purpose-driven, and well-versed experts working in the various areas of publishing, eager to help open your eyes to the promise of publishing and effortlessly guide you through the process.

Colors
0094D4
00A9DD
6FCCEA
C7EBF8
E9F6FB
FFF300
FFF600
FEFA6F
FFFEC7
FFFEE8
FFC000
F8CF3A
FAE287
FDF2CF
FEFAEE
F0912C
F2A743
F7CA91
FBE8D2
FDF5EE
EE7325
F08F49
F5BC92
FAE3D3
FDF4ED
6B429C
8869AF
B7A5CE
E3DAEB
F3F0F8

```html
<!DOCTYPE html>
<html lang="en">
<head>
<meta charset="utf-8">
<title>Write Onward! – Cover Options</title>
<link rel="stylesheet" href="https://fonts.googleapis.com/css2?family=Exo+2:wght@600&family=Russo+One&display=swap">
<style>
  :root {
    --page: #ffffff;
    --cover-purple: #6B449A;
    --cover-orange: #F05A28;
    --ink: #ffffff;
  }
  html, body {
    margin: 0;
    padding: 0;
    width: 1200px;
    height: 896px;
    overflow: hidden;
    background: var(--page);
  }
  .cover-sheet {
    display: block;
    width: 1200px;
    height: 896px;
  }
  .cover-bg--purple { fill: var(--cover-purple); }
  .cover-bg--orange { fill: var(--cover-orange); }
  .frame-bar { fill: var(--ink); }
  .title-line {
    fill: var(--ink);
    font-family: "Russo One", sans-serif;
    font-size: 140px;
  }
  .subtitle-line {
    fill: var(--ink);
    font-family: "Russo One", sans-serif;
    font-size: 25px;
  }
  .author-name {
    fill: var(--ink);
    font-family: "Exo 2", sans-serif;
    font-weight: 600;
    font-size: 19px;
    letter-spacing: 0.5px;
  }
</style>
</head>
<body>
<svg class="cover-sheet" viewBox="0 0 1200 896" xmlns="http://www.w3.org/2000/svg" xmlns:xlink="http://www.w3.org/1999/xlink" role="img" aria-label="Two colour options for the front cover of Write Onward! Veteran Editors Reveal Their Methods">
  <defs>
    <symbol id="cover-layout" viewBox="0 0 576 864" width="576" height="864">
      <!-- framing brackets -->
      <g class="frame">
        <rect class="frame-bar" x="80" y="93" width="90" height="10"/>
        <rect class="frame-bar" x="410" y="93" width="93" height="10"/>
        <rect class="frame-bar" x="80" y="93" width="10" height="92"/>
        <rect class="frame-bar" x="493" y="93" width="10" height="92"/>
        <rect class="frame-bar" x="80" y="416" width="10" height="31"/>
        <rect class="frame-bar" x="493" y="416" width="10" height="31"/>
        <rect class="frame-bar" x="80" y="679" width="10" height="93"/>
        <rect class="frame-bar" x="493" y="679" width="10" height="93"/>
        <rect class="frame-bar" x="80" y="762" width="90" height="10"/>
        <rect class="frame-bar" x="410" y="762" width="93" height="10"/>
      </g>

      <!-- author name slots -->
      <text class="author-name" x="289" y="105" text-anchor="middle">AUTHOR NAME 1</text>
      <text class="author-name" x="289" y="774" text-anchor="middle">AUTHOR NAME 2</text>
      <text class="author-name" transform="translate(92 558) rotate(-90)" text-anchor="middle">AUTHOR NAME 3</text>
      <text class="author-name" transform="translate(92 307) rotate(-90)" text-anchor="middle">AUTHOR NAME 4</text>
      <text class="author-name" transform="translate(491 297) rotate(90)" text-anchor="middle">AUTHOR NAME 5</text>
      <text class="author-name" transform="translate(491 558) rotate(90)" text-anchor="middle">AUTHOR NAME 6</text>

      <!-- stacked title -->
      <text class="title-line" x="125" y="246" textLength="300" lengthAdjust="spacingAndGlyphs">WRI</text>
      <text class="title-line" x="125" y="375" textLength="215" lengthAdjust="spacingAndGlyphs">TE</text>
      <text class="title-line" x="125" y="505" textLength="225" lengthAdjust="spacingAndGlyphs">ON</text>
      <text class="title-line" x="125" y="635" textLength="330" lengthAdjust="spacingAndGlyphs">WARD!</text>

      <!-- subtitle -->
      <text class="subtitle-line" x="125" y="681" textLength="300" lengthAdjust="spacingAndGlyphs">VETERAN EDITORS</text>
      <text class="subtitle-line" x="125" y="712" textLength="325" lengthAdjust="spacingAndGlyphs">REVEAL THEIR METHODS</text>
    </symbol>
  </defs>

  <g class="cover cover--purple" transform="translate(17 17)">
    <rect class="cover-bg--purple" width="576" height="864"/>
    <use xlink:href="#cover-layout" href="#cover-layout" x="0" y="0" width="576" height="864"/>
  </g>

  <g class="cover cover--orange" transform="translate(607 17)">
    <rect class="cover-bg--orange" width="576" height="864"/>
    <use xlink:href="#cover-layout" href="#cover-layout" x="0" y="0" width="576" height="864"/>
  </g>
</svg>
</body>
</html>
```